Copperleaf Motorized Shade Business Card

Hello, we've had our logo made. Now we are looking for a clean and cool looking business card. One side can just be the logo with any design elements that might look good with it. The other side will be Name, Phone Number and Email. There will not be an address on the card.

```html
<!DOCTYPE html>
<html lang="en">
<head>
<meta charset="utf-8">
<title>Copperleaf Motorized Shade Business Card</title>
<link href="https://fonts.googleapis.com/css2?family=Oswald:wght@600&family=Roboto:wght@400;500&display=swap" rel="stylesheet">
<style>
  :root {
    --navy: #003d75;
    --sky: #00aeef;
    --sun: #fdc010;
    --paper: #ffffff;
    --page: #ffffff;
  }
  * { margin: 0; padding: 0; box-sizing: border-box; }
  html, body { width: 1200px; height: 1200px; overflow: hidden; background: var(--page); }
  .canvas { position: relative; width: 1200px; height: 1200px; }

  .card { position: absolute; left: 258px; width: 698px; height: 399px; overflow: hidden; }
  .card > svg { position: absolute; inset: 0; width: 100%; height: 100%; display: block; }
  .card-front { top: 153px; background: var(--paper); box-shadow: 0 8px 18px rgba(0,0,0,0.18); }
  .card-back { top: 638px; background: var(--navy); box-shadow: 0 8px 18px rgba(0,0,0,0.18); }

  .brand {
    position: absolute; left: 75px; top: 184px; width: 230px;
    text-align: center; line-height: 1;
  }
  .brand-name {
    display: block; font-family: "Oswald", sans-serif; font-weight: 600;
    font-size: 44px; letter-spacing: 0.5px; color: var(--navy); text-transform: uppercase;
  }
  .brand-line {
    display: block; margin-top: 18px; font-family: "Roboto", sans-serif; font-weight: 500;
    font-size: 11.5px; letter-spacing: 5px; color: var(--sky); text-transform: uppercase;
  }

  .holder {
    position: absolute; left: 90px; top: 158px;
    font-family: "Oswald", sans-serif; font-weight: 600; font-size: 47px;
    color: var(--paper); line-height: 1; letter-spacing: 0.5px;
  }
  .contact {
    position: absolute; left: 297px; display: flex; align-items: center; gap: 12px;
    font-family: "Roboto", sans-serif; font-size: 18px; color: var(--paper);
  }
  .contact svg { width: 29px; height: 29px; flex: none; }
  .contact-email { top: 146px; }
  .contact-phone { top: 193px; font-size: 17px; }
  .website {
    position: absolute; left: 62px; top: 362px;
    font-family: "Roboto", sans-serif; font-size: 15.5px; color: var(--navy);
  }
</style>
</head>
<body>
<main class="canvas">

  <section class="card card-front" aria-label="Card front">
    <svg viewBox="0 0 1116 638" preserveAspectRatio="none" role="img" aria-label="Angled decorative panel in navy, sky blue and sunny yellow">
      <defs>
        <linearGradient id="panel-tone" x1="0" y1="0" x2="1" y2="1">
          <stop offset="0" stop-color="var(--navy)"/>
          <stop offset="0.55" stop-color="var(--sky)"/>
          <stop offset="1" stop-color="var(--sun)"/>
        </linearGradient>
      </defs>
      <polygon fill="url(#panel-tone)" points="618,0 1116,0 1116,638 451,638"/>
    </svg>
    <h1 class="brand">
      <span class="brand-name">Copperleaf</span>
      <span class="brand-line">Motorized Shades</span>
    </h1>
  </section>

  <section class="card card-back" aria-label="Card back">
    <svg viewBox="0 0 1116 638" preserveAspectRatio="none" aria-hidden="true">
      <rect fill="var(--sun)" x="575" y="598" width="541" height="14"/>
      <circle fill="var(--sun)" cx="297" cy="716" r="301"/>
    </svg>

    <h2 class="holder">John Doe</h2>

    <p class="contact contact-email">
      <svg viewBox="0 0 29 29" aria-hidden="true">
        <rect x="1.5" y="4.5" width="26" height="20" fill="none" stroke="var(--paper)" stroke-width="1.4"/>
        <polyline points="1.5,4.5 14.5,15.5 27.5,4.5" fill="none" stroke="var(--paper)" stroke-width="1.4"/>
        <line x1="1.5" y1="24.5" x2="11" y2="13" stroke="var(--paper)" stroke-width="1.4"/>
        <line x1="27.5" y1="24.5" x2="18" y2="13" stroke="var(--paper)" stroke-width="1.4"/>
      </svg>
      <span>john.doe@copperleafmotorizedshade.com</span>
    </p>

    <p class="contact contact-phone">
      <svg viewBox="0 0 29 29" aria-hidden="true">
        <path d="M2 9 C2 3 27 3 27 9 L27 11 L22 11 L22 8 L7 8 L7 11 L2 11 Z" fill="none" stroke="var(--paper)" stroke-width="1.3"/>
        <path d="M9 10 L20 10 L25 27 L4 27 Z" fill="none" stroke="var(--paper)" stroke-width="1.3"/>
        <g fill="var(--paper)">
          <rect x="11" y="15" width="1.8" height="1.8"/><rect x="13.6" y="15" width="1.8" height="1.8"/><rect x="16.2" y="15" width="1.8" height="1.8"/>
          <rect x="11" y="18" width="1.8" height="1.8"/><rect x="13.6" y="18" width="1.8" height="1.8"/><rect x="16.2" y="18" width="1.8" height="1.8"/>
          <rect x="11" y="21" width="1.8" height="1.8"/><rect x="13.6" y="21" width="1.8" height="1.8"/><rect x="16.2" y="21" width="1.8" height="1.8"/>
        </g>
      </svg>
      <span>+01 123456789</span>
    </p>

    <p class="website">www.copperleafmotorizedshade.com</p>
  </section>

</main>
</body>
</html>
```